Business Card Design Project

I own a dental practice and would like to use a logo that was recently designed to make business cards.
I am looking for a clean card with the following information on the card.

Halvorsen Dental Center (Using the logo)
Martin K. Halvorsen, D.D.S.
2847 Willow Bend Rd. Suite B
Colorado Springs, CO 80471
(719) 555-0186
halvorsendentalcenter@mailnest.example
www.halvorsendentalcenter.example

Also a list of items on the back:
Services include

Family Dentistry
Cosmetic
Whitening
Tooth Colored Fillings
Crowns/Bridges
Implants/Tooth Replacement
Dentures
Root Canals
Updates

Just an FYI, I added an email address and website address.

I also added my Pic.  Please give designs with and without the pic

Thanks

Target Market(s)

20-70 U.S. Female that handles the household budget.

Industry/Entity Type

Dental

Requirements
Must have
• The logo is key. The color scheme of the logo is also key. The back of the business card should have the list of Dental Services offered at the practice. The front should be clean and professional looking. No cartoons. I will also include a picture of myself. I think that the final card may or may not include this picture, so the card designs should come with and without the picture. USE THE BLUE LOGO ONLY!!!
Should not have
• NO teeth should be on the card.

```html
<!DOCTYPE html>
<html lang="en">
<head>
<meta charset="utf-8">
<title>Halvorsen Dental Center – Business Cards</title>
<link rel="stylesheet" href="https://fonts.googleapis.com/css2?family=Pathway+Gothic+One&display=swap">
<style>
  :root {
    --navy-black: #05060f;
    --royal-blue: #1b3fd6;
    --bright-blue: #2f5cff;
    --silver-light: #e6e7ea;
    --silver-dark: #8d9096;
    --card-white: #f6f7f8;
    --back-grey-light: #eceeee;
    --back-grey-dark: #d3d6d6;
    --ink: #2a2a2a;
    --logo-blue: #3fa9e0;
    --cyan: #33e4f2;
    --photo-suit: #24262d;
    --photo-shirt: #c9cbe0;
    --photo-skin: #c99a80;
  }
  * { margin: 0; padding: 0; box-sizing: border-box; }
  html, body { width: 1200px; height: 711px; overflow: hidden; background: #ffffff; }
  body { position: relative; font-family: "Pathway Gothic One", "Arial Narrow", sans-serif; color: var(--ink); }

  .card { position: absolute; overflow: hidden; }
  .card--front { width: 585px; background: var(--card-white); }
  .card--back {
    width: 586px;
    background: linear-gradient(90deg, var(--back-grey-dark) 0%, var(--back-grey-light) 45%, var(--back-grey-light) 100%);
  }
  .card--a { left: 3px; top: 0; height: 340px; }
  .card--b { left: 614px; top: 0; height: 340px; }
  .card--c { left: 3px; top: 372px; height: 339px; }
  .card--d { left: 614px; top: 372px; height: 339px; }

  .band {
    position: absolute; left: 0; width: 100%;
    background: linear-gradient(90deg, var(--navy-black) 0%, var(--royal-blue) 45%, var(--bright-blue) 62%, var(--royal-blue) 80%, var(--navy-black) 100%);
  }
  .stripe {
    position: absolute; left: 0; width: 100%;
    background: linear-gradient(180deg, var(--silver-light), var(--silver-dark));
  }

  .logo { position: absolute; display: flex; align-items: center; gap: 10px; }
  .logo__dot { width: 34px; height: 34px; border-radius: 50%; background: var(--logo-blue); flex: none; }
  .logo__name { font-size: 30px; color: var(--logo-blue); white-space: nowrap; letter-spacing: 0.5px; }

  .text { position: absolute; white-space: nowrap; }
  .doctor-name { font-size: 32px; color: var(--ink); letter-spacing: 0.3px; }
  .doctor-name--beside-photo { font-size: 28px; letter-spacing: 0; }
  .contact { font-size: 18px; line-height: 23px; color: var(--ink); }
  .website { font-size: 19px; color: #ffffff; letter-spacing: 0.5px; }
  .website--cyan { color: var(--cyan); font-size: 20px; letter-spacing: 1px; }

  .services { position: absolute; right: 34px; top: 36px; text-align: right; }
  .services__title { font-size: 27px; line-height: 34px; margin-bottom: 6px; font-weight: 400; }
  .services__list { list-style: none; }
  .services__item { font-size: 19.5px; line-height: 27.7px; }
  .services--dark { color: var(--ink); }
  .services--cyan { color: var(--cyan); }

  .portrait {
    position: absolute; left: 432px; top: 58px; width: 153px; height: 218px;
    background: linear-gradient(180deg, var(--photo-skin) 0%, #a98472 35%, var(--photo-shirt) 55%, var(--photo-suit) 75%, var(--photo-suit) 100%);
  }
</style>
</head>
<body>

  <section class="card card--front card--a">
    <div class="band" style="top:0;height:50px"></div>
    <div class="stripe" style="top:50px;height:10px"></div>
    <div class="logo" style="left:18px;top:196px">
      <span class="logo__dot"></span>
      <span class="logo__name">Halvorsen Dental Center</span>
    </div>
    <div class="text doctor-name" style="right:16px;top:80px">Martin K. Halvorsen, D.D.S.</div>
    <div class="text contact" style="right:18px;top:118px">(719) 555-0186</div>
    <div class="text contact" style="right:18px;top:151px;text-align:right">2847 Willow Bend Rd. Suite B<br>Colorado Springs, CO 80471</div>
    <div class="text contact" style="right:18px;top:219px">halvorsendentalcenter@mailnest.example</div>
    <div class="stripe" style="top:277px;height:10px"></div>
    <div class="band" style="top:287px;height:53px"></div>
    <div class="text website" style="left:0;width:100%;text-align:center;top:300px">www.halvorsendentalcenter.example</div>
  </section>

  <section class="card card--back card--b">
    <div class="logo" style="left:18px;top:156px">
      <span class="logo__dot"></span>
      <span class="logo__name">Halvorsen Dental Center</span>
    </div>
    <div class="services services--dark">
      <h2 class="services__title">Services include</h2>
      <ul class="services__list">
        <li class="services__item">Family Dentistry</li>
        <li class="services__item">Cosmetic</li>
        <li class="services__item">Whitening</li>
        <li class="services__item">Tooth Colored Fillings</li>
        <li class="services__item">Crowns/Bridges</li>
        <li class="services__item">Implants/Tooth Replacement</li>
        <li class="services__item">Dentures</li>
        <li class="services__item">Root Canals</li>
      </ul>
    </div>
  </section>

  <section class="card card--front card--c">
    <div class="band" style="top:0;height:50px"></div>
    <div class="stripe" style="top:50px;height:8px"></div>
    <div class="portrait" role="img" aria-label="Portrait photograph of the dentist in a dark suit and lilac tie"></div>
    <div class="logo" style="left:8px;top:92px">
      <span class="logo__dot"></span>
      <span class="logo__name">Halvorsen Dental Center</span>
    </div>
    <div class="text doctor-name doctor-name--beside-photo" style="left:196px;top:166px">Martin K. Halvorsen, D.D.S.</div>
    <div class="text contact" style="left:22px;top:179px;font-size:17px">(719) 555-0186<br>2847 Willow Bend Rd. Suite B<br>Colorado Springs, CO 80471<br>halvorsendentalcenter@mailnest.example</div>
    <div class="stripe" style="top:276px;height:9px"></div>
    <div class="band" style="top:285px;height:54px"></div>
    <div class="text website website--cyan" style="right:16px;top:298px">www.halvorsendentalcenter.example</div>
  </section>

  <section class="card card--back card--d">
    <div class="logo" style="left:22px;top:128px">
      <span class="logo__dot"></span>
      <span class="logo__name">Halvorsen Dental Center</span>
    </div>
    <div class="services services--cyan">
      <h2 class="services__title">Services include</h2>
      <ul class="services__list">
        <li class="services__item">Family Dentistry</li>
        <li class="services__item">Cosmetic</li>
        <li class="services__item">Whitening</li>
        <li class="services__item">Tooth Colored Fillings</li>
        <li class="services__item">Crowns/Bridges</li>
        <li class="services__item">Implants/Tooth Replacement</li>
        <li class="services__item">Dentures</li>
        <li class="services__item">Root Canals</li>
      </ul>
    </div>
  </section>

</body>
</html>
```